Implant and Mini Implant trifold brochure.

Logo is attached. Our website: www.q7rdental.com

We need an Implant and Mini Implant Flyer (on the same flyer) to be done by someone experienced in Dental marketing.

To be mailed via : Each Block Bulk Post-Counter® (EBBP Counter®)
You need to put a Retail Indica
Reference: https://www.natpostal.example/business/each-block-bulk-post.htm
Each Block Bulk Post-Counter Indicia Guidelines

Every EBBP mailpiece must have an EBBP indicia with “ECRWSS” in the address area, within the permit indicia, or below the permit, like the examples to the right.
The EBBP Counter Indicia does not have a specific size requirement but must be larger than .5" x .5".
The type font must be in all caps and at least a 4 point size.
Place the indicia in the upper right hand corner of the mailpiece.
It should fit in the area 1.625" from the right edge and 1.375" from top edge.
Leave 1/8" of space around the top and right edge.

There should be a picture of a senior citizen eating apple - that is what implants will provide.

One side English; Other side Spanish.

If you do not have idea on what implants and mini-implants are then please ask specific questions.

Make space for specials.

Target Market(s)

dental implants, dental mini implants

Font styles to use
Other font styles liked:
• leaving it open for designer.

Colors
00a990
33b8a4
87cfc6
cadf82

Requirements
Must have
• A senior citizen eating apple - that is what implants allow people to do.
• Once the design layout is finalized, we will provide text. I am leaving the design wide open. you may look at good templates for ideas, but please respect the copyright.
Nice to have
• Use implant and mini implant pictures.
• Images needed
• 1) 3 Easy Steps to Implant Restoration in 1 visit: Use three images: mouth with missing teeth; mouth with implant screws fitted; mouth with teeth restored.
• 2) Image for Implant based Denture.
• 3) Senior Citizen or a couple eating apple.
• Image must be of good quality; even if taken from different sources they must gel well with the over all design. The final design has to be stunning.
• Please do not provide me with designs that I can get from any printing company.
• The Text area:
• 1. Why Implants?
• 2. Space for implant based dentures.
• 3. Other spaces for filling in "Why visit q7r Dental"
• Additional Info: Time to use the following text in the final output.
• q7r Dental - Your base for Crown-to-Root Dental care.
• q7r Dental - Your Implant Harbor.
• Why Implants?
• . Durable, long lasting teeth replacement
• . Surgically implanted metal posts or frames into the jawbone
• . Allows crowns, bridges or complete dentures to be placed on implants
• Why Implant Dentures?
• . Durable and Cost Effective
• . Your denture fabricated as normal denture
• . Four or more implants are placed in one visit
• . Your denture is then retrofitted to snap on the mini implant retention head
• . Stabilize your loose dentures in one visit
• Why Mini Implants?
• . Less involved procedure than conventional implants
• . Usually completed in one dental appointment
• . Replace missing teeth instantly
• Implants vs Mini-Implants
• Visit q7r Dental for a complementary consultation to learn which option is best for you. Depending on various conditions including that of the jawbone, you may be recommended an implant or mini-implant based treatment.
• Implant or Mini-implant treatment may not be suitable for all patients. For implants to be successful, you need to have healthy gums and adequate bones to support the implants. You must also be willing to commit to proper maintenance of your implants or dentures. Visit your dentist at q7r Dental to learn more.
• Spanish translation from google added below:
• q7r Dental: su base para atención Corona-a-Raíz dental.
• q7r Dental: su puerto de implante.
• ¿Por qué los implantes?
• . Reemplazo duradero y duradero de los dientes
• . Puestos o marcos de metal implantados quirúrgicamente en la mandíbula
• . Permiten para colocan coronas, puentes o dentaduras completas en implantes
• ¿Por qué las dentaduras postizas?
• . Durable y rentable
• . Su dentadura fabricada como dentadura normal
• . Cuatro o más implantes se colocan en una visita
• . Su dentadura se reajusta para encajar en el cabezal de retención mini implante
• . Estabilice sus dentaduras sueltas en una visita
• ¿Por qué Mini Implantes?
• . Procedimiento menos complicado que los implantes convencionales
• . Generalmente se completa en una cita dental
• . Reemplace los dientes perdidos al
• Implantes vs Mini Implantes
• Visite q7r Dental para obtener una consulta complementaria y conocer cuál es la mejor opción para usted. Dependiendo de varias condiciones, incluida de la mandíbula, se le puede recomenda un tratamiento basado en implantes o mini-implantes.
• El tratamiento con implantes o mini-implantes puede no ser adecuado para todos los pacientes. Para que los implantes tengan éxito, debe tener encías sanas y huesos adecuados para apoyar los implantes. También debe estar dispuesto a comprometerse con el mantenimiento adecuado de sus implantes o dentaduras postizas. Visite a su dentista en q7r Dental para obtener más información.
Should not have
• blank spaces without purpose

```html
<!DOCTYPE html>
<html lang="en">
<head>
<meta charset="utf-8">
<title>q7r Dental — Implants Trifold</title>
<link href="https://fonts.googleapis.com/css2?family=Montserrat:wght@400;600;700;800&family=Open+Sans:wght@400;600&family=Lora:ital@0;1&display=swap" rel="stylesheet">
<style>
  :root{
    --teal:#00a990;
    --teal-2:#33b8a4;
    --mint:#87cfc6;
    --lime:#cadf82;
    --lime-deep:#b7d35e;
    --backdrop:#47cfb8;
    --ink:#3b3f44;
    --muted:#7b8186;
    --paper:#ffffff;
    --fold:#e3e6e6;
  }
  *{box-sizing:border-box;margin:0;padding:0}
  html,body{width:878px;height:1200px;overflow:hidden}
  body{background:var(--backdrop);position:relative;font-family:"Open Sans",Arial,sans-serif;color:var(--ink)}
  .brochure{position:absolute;left:70px;width:738px;height:570px;background:var(--paper);box-shadow:0 8px 24px rgba(0,60,50,.25);overflow:hidden}
  .brochure--es{top:30px}
  .brochure--en{top:620px}
  .brochure__art{position:absolute;inset:0;width:738px;height:570px}
  .t{position:absolute;line-height:1.2}
  .cover-title{left:0;width:232px;text-align:right;top:16px;color:var(--teal);font-size:19px;font-family:"Montserrat",sans-serif;font-weight:800}
  .cover-sub{left:0;width:232px;text-align:right;top:39px;font-size:9px;font-family:"Montserrat",sans-serif;color:var(--ink);letter-spacing:.5px}
  .brand-line{left:18px;top:150px;width:212px;font-family:"Montserrat",sans-serif;border-bottom:1px solid var(--teal-2);padding-bottom:3px}
  .brand-line b{display:block;color:var(--lime-deep);font-size:14px;font-weight:800}
  .brand-line span{display:block;color:var(--teal);font-size:11px;letter-spacing:.4px}
  .section-title{font-family:"Montserrat",sans-serif;font-weight:800;font-size:11px;color:var(--ink);text-transform:uppercase}
  .section-sub{font-size:8px;color:var(--teal);font-weight:600}
  .body-copy{font-size:7px;line-height:1.4;color:var(--muted)}
  .how{left:18px;top:196px;width:212px}
  .types{left:18px;top:304px;width:212px}
  .types .section-title{border-bottom:1px solid var(--teal-2);padding-bottom:3px;margin-bottom:4px}
  .type-item{display:flex;gap:5px;margin-top:4px}
  .type-item svg{flex:none;margin-top:1px}
  .type-item .name{font-size:8px;font-weight:600;color:var(--lime-deep)}
  .type-item--narrow{width:130px}
  .promise{left:24px;top:512px;font-family:"Montserrat",sans-serif;color:var(--ink);font-size:12px}
  .promise b{display:block;color:var(--teal);font-weight:800;font-size:14px}
  .reviews{left:262px;top:170px;width:214px}
  .reviews .label{font-family:"Montserrat",sans-serif;font-size:10px;color:var(--ink);border-bottom:1px solid var(--teal-2);padding-bottom:2px;width:120px}
  .reviews .label b{font-weight:800;display:block}
  .quote{display:flex;gap:6px;margin-top:8px;align-items:flex-start}
  .quote-mark{font-family:"Montserrat",sans-serif;font-weight:800;color:var(--teal);font-size:24px;line-height:.8}
  .quote p{font-family:"Lora",serif;font-size:7.5px;color:var(--muted);line-height:1.35}
  .quote cite{display:block;text-align:right;font-style:normal;font-weight:700;color:var(--teal);font-family:"Montserrat",sans-serif;font-size:7.5px;margin-top:2px}
  .contact{left:262px;top:412px;width:214px}
  .contact .section-title{color:var(--teal);font-size:14px}
  .contact .lead{font-size:7.5px;color:var(--ink);margin-bottom:8px}
  .offices{display:flex;gap:12px}
  .office{flex:1}
  .office h4{font-family:"Montserrat",sans-serif;font-size:7px;font-weight:700;color:var(--teal);text-transform:uppercase;margin-bottom:4px}
  .office-row{display:flex;gap:4px;align-items:flex-start;font-size:6.8px;line-height:1.3;color:var(--ink);margin-bottom:5px}
  .office-row svg{flex:none}
  .brand-name{left:508px;top:24px;font-family:"Montserrat",sans-serif;font-weight:700;font-size:18px;color:var(--ink);letter-spacing:.3px}
  .tagline{left:508px;top:76px;width:130px}
  .tagline small{font-family:"Lora",serif;font-style:italic;font-size:9px;color:var(--muted);display:block}
  .tagline b{font-family:"Montserrat",sans-serif;font-weight:700;font-size:14px;color:var(--teal);display:block;line-height:1.15}
  .website{left:520px;top:492px;transform:rotate(-14deg);transform-origin:left center;background:var(--paper);padding:4px 12px;font-family:"Montserrat",sans-serif;font-weight:700;font-size:11px;color:var(--teal)}
</style>
</head>
<body>

<svg width="0" height="0" style="position:absolute" aria-hidden="true">
  <defs>
    <linearGradient id="mouthTone" x1="0" y1="0" x2="1" y2="1">
      <stop offset="0" stop-color="#d59a86"/><stop offset=".55" stop-color="#b8524a"/><stop offset="1" stop-color="#e7b9a6"/>
    </linearGradient>
    <radialGradient id="lensTone"><stop offset="0" stop-color="#efe9e4"/><stop offset="1" stop-color="#b89c92"/></radialGradient>
    <radialGradient id="patientTone"><stop offset="0" stop-color="#f2d9cc"/><stop offset="1" stop-color="#c9d6d9"/></radialGradient>
    <radialGradient id="seniorTone"><stop offset="0" stop-color="#e9c7b4"/><stop offset=".6" stop-color="#9b7a66"/><stop offset="1" stop-color="#d8d8d8"/></radialGradient>
    <radialGradient id="modelTone"><stop offset="0" stop-color="#ffffff"/><stop offset="1" stop-color="#efb9b5"/></radialGradient>
    <clipPath id="coverClip"><rect x="492" y="0" width="246" height="570"/></clipPath>
    <symbol id="tooth" viewBox="0 0 10 10"><path d="M2 1c1.2-.6 2 .2 3 .2S6.8.4 8 1c1.4.8 1 3-.2 4.2L7 9c-.3.8-1 .6-1.1-.2L5.4 6.5h-.8L4.1 8.8C4 9.6 3.3 9.8 3 9L2.2 5.2C1 4 .6 1.8 2 1z" fill="var(--teal)"/></symbol>
    <symbol id="pin" viewBox="0 0 10 12"><path d="M5 0a4 4 0 0 1 4 4c0 3-4 8-4 8S1 7 1 4a4 4 0 0 1 4-4zm0 2.3a1.7 1.7 0 1 0 0 3.4 1.7 1.7 0 0 0 0-3.4z" fill="var(--teal)"/></symbol>
    <symbol id="phone" viewBox="0 0 12 12"><path d="M2.5 1l2 2.3-1.2 1.4a7 7 0 0 0 4 4l1.4-1.2L11 9.5 9.8 11C5 10.8 1.2 7 1 2.2z" fill="var(--teal)"/></symbol>
  </defs>
</svg>

<!-- ============ SPANISH ============ -->
<section class="brochure brochure--es" lang="es">
  <svg class="brochure__art" viewBox="0 0 738 570" aria-hidden="true">
    <path d="M0 0H246V58Q120 70 0 128Z" fill="var(--lime)"/>
    <path d="M0 140Q110 86 246 70" fill="none" stroke="var(--teal)" stroke-width="6"/>
    <path d="M0 150Q110 98 246 82" fill="none" stroke="var(--mint)" stroke-width="3"/>
    <path d="M0 570V522Q130 488 246 418V570Z" fill="var(--lime)"/>
    <path d="M0 512Q130 476 246 406" fill="none" stroke="var(--teal)" stroke-width="6"/>
    <path d="M246 0H492V118Q380 172 246 150Z" fill="url(#mouthTone)"/>
    <path d="M246 392Q370 352 492 298V570H246Z" fill="var(--lime)"/>
    <path d="M246 382Q370 342 492 288" fill="none" stroke="var(--teal)" stroke-width="6"/>
    <path d="M492 570V430Q620 392 738 312V570Z" fill="var(--lime)"/>
    <path d="M492 420Q620 382 738 300" fill="none" stroke="var(--teal-2)" stroke-width="5"/>
    <line x1="246" y1="0" x2="246" y2="570" stroke="var(--fold)"/>
    <line x1="492" y1="0" x2="492" y2="570" stroke="var(--fold)"/>
  </svg>
  <svg class="brochure__art" viewBox="0 0 738 570">
    <circle cx="432" cy="118" r="42" fill="url(#lensTone)" stroke="#fff" stroke-width="4" role="img" aria-label="Lupa sobre un implante dental"/>
    <circle cx="290" cy="318" r="7" fill="var(--teal)"/>
    <circle cx="312" cy="318" r="7" fill="var(--mint)"/>
    <circle cx="370" cy="322" r="40" fill="url(#patientTone)" stroke="#fff" stroke-width="4" role="img" aria-label="Foto de una paciente en revisión dental"/>
    <circle cx="196" cy="432" r="48" fill="url(#modelTone)" stroke="#fff" stroke-width="4" role="img" aria-label="Modelo de dientes con implante"/>
    <g clip-path="url(#coverClip)"><circle cx="660" cy="262" r="124" fill="url(#seniorTone)" stroke="#fff" stroke-width="5" role="img" aria-label="Foto de un hombre mayor comiendo una manzana roja"/></g>
  </svg>

  <div class="t cover-title">IMPLANTES</div>
  <div class="t cover-sub">MINI-IMPLANTES</div>
  <div class="t brand-line"><b>Q7R DENTAL</b><span>SU PUERTO DENTAL</span></div>
  <div class="t how">
    <div class="section-title">Cómo hacer</div>
    <div class="section-sub">¿Cómo funcionan los implantes dentales?</div>
    <p class="body-copy">Debido a que los implantes se fusionan a su mandíbula, proporcionan un soporte estable para dientes artificiales. Las dentaduras y puentes montados en implantes no se deslizarán ni cambiarán en la boca al comer y hablar. Este ajuste seguro ayuda a que coronas y dentaduras se sientan más naturales que las convencionales.</p>
  </div>
  <div class="t types">
    <div class="section-title">Tipos de implantes</div>
    <div class="type-item"><svg width="10" height="10"><use href="#tooth"/></svg><div><div class="name">Implantes Endosteal</div><p class="body-copy">Se implantan quirúrgicamente en la mandíbula. Cuando la encía sana, una segunda cirugía conecta un poste al implante.</p></div></div>
    <div class="type-item type-item--narrow"><svg width="10" height="10"><use href="#tooth"/></svg><div><div class="name">Implantes subperiósticos</div><p class="body-copy">Un marco de metal se ajusta en la mandíbula debajo de la encía. Al sanar, el marco queda fijo y sus postes sobresalen de las encías.</p></div></div>
  </div>
  <div class="t promise"><b>TE APOSTAMOS,</b>NO VA A DOLER!</div>

  <div class="t reviews">
    <div class="label"><b>QUÉ</b>LA GENTE DICE</div>
    <div class="quote"><span class="quote-mark">“</span><div><p>Simplemente increíble y muy bien informada. Me hice limpiar los dientes en el militar, pero ella realmente hizo un trabajo increíble.</p><cite>- Dana R, paciente</cite></div><span class="quote-mark">”</span></div>
  </div>
  <div class="t contact">
    <div class="section-title">Estar en contacto</div>
    <div class="lead">Nos encantaría saber de usted</div>
    <div class="offices">
      <div class="office"><h4>Larkton, MD</h4>
        <div class="office-row"><svg width="8" height="10"><use href="#pin"/></svg><span>418 Harbor Mill Rd,<br>Larkton, MD 20700</span></div>
        <div class="office-row"><svg width="9" height="9"><use href="#phone"/></svg><span>240-555-0142<br>1-800-555-0168</span></div></div>
      <div class="office"><h4>Brookvale, MD</h4>
        <div class="office-row"><svg width="8" height="10"><use href="#pin"/></svg><span>7731 Fernway Rd,<br>Brookvale, MD 20800</span></div>
        <div class="office-row"><svg width="9" height="9"><use href="#phone"/></svg><span>301-555-0193<br>1-800-555-0177</span></div></div>
    </div>
  </div>

  <div class="t brand-name">q7r Dental</div>
  <div class="t tagline"><small>Mereces nada menos ...</small><b>Una hermosa<br>Sonreír</b></div>
  <div class="t website">www.q7rdental.com</div>
</section>

<!-- ============ ENGLISH ============ -->
<section class="brochure brochure--en" lang="en">
  <svg class="brochure__art" viewBox="0 0 738 570" aria-hidden="true">
    <path d="M0 0H246V58Q120 70 0 128Z" fill="var(--lime)"/>
    <path d="M0 140Q110 86 246 70" fill="none" stroke="var(--teal)" stroke-width="6"/>
    <path d="M0 150Q110 98 246 82" fill="none" stroke="var(--mint)" stroke-width="3"/>
    <path d="M0 570V522Q130 488 246 418V570Z" fill="var(--lime)"/>
    <path d="M0 512Q130 476 246 406" fill="none" stroke="var(--teal)" stroke-width="6"/>
    <path d="M246 0H492V118Q380 172 246 150Z" fill="url(#mouthTone)"/>
    <path d="M246 392Q370 352 492 298V570H246Z" fill="var(--lime)"/>
    <path d="M246 382Q370 342 492 288" fill="none" stroke="var(--teal)" stroke-width="6"/>
    <path d="M492 570V430Q620 392 738 312V570Z" fill="var(--lime)"/>
    <path d="M492 420Q620 382 738 300" fill="none" stroke="var(--teal-2)" stroke-width="5"/>
    <line x1="246" y1="0" x2="246" y2="570" stroke="var(--fold)"/>
    <line x1="492" y1="0" x2="492" y2="570" stroke="var(--fold)"/>
  </svg>
  <svg class="brochure__art" viewBox="0 0 738 570">
    <circle cx="432" cy="118" r="42" fill="url(#lensTone)" stroke="#fff" stroke-width="4" role="img" aria-label="Magnifier over a dental implant"/>
    <circle cx="290" cy="318" r="7" fill="var(--teal)"/>
    <circle cx="312" cy="318" r="7" fill="var(--mint)"/>
    <circle cx="370" cy="322" r="40" fill="url(#patientTone)" stroke="#fff" stroke-width="4" role="img" aria-label="Photo of a patient at a dental check-up"/>
    <circle cx="196" cy="432" r="48" fill="url(#modelTone)" stroke="#fff" stroke-width="4" role="img" aria-label="Teeth model with an implant"/>
    <g clip-path="url(#coverClip)"><circle cx="660" cy="262" r="124" fill="url(#seniorTone)" stroke="#fff" stroke-width="5" role="img" aria-label="Photo of a senior man eating a red apple"/></g>
  </svg>

  <div class="t cover-title">IMPLANTS</div>
  <div class="t cover-sub">MINI-IMPLANTS</div>
  <div class="t brand-line"><b>Q7R DENTAL</b><span>YOUR DENTAL HARBOR</span></div>
  <div class="t how">
    <div class="section-title">How do</div>
    <div class="section-sub">Dental Implants Work?</div>
    <p class="body-copy">Because implants fuse to your jawbone, they provide stable support for artificial teeth. Dentures and bridges mounted to implants won't slip or shift in your mouth — an especially important benefit when eating and speaking. This secure fit helps the dentures and bridges — as well as individual crowns placed over implants — feel more natural than conventional bridges or dentures.</p>
  </div>
  <div class="t types">
    <div class="section-title">Types of implants</div>
    <div class="type-item"><svg width="10" height="10"><use href="#tooth"/></svg><div><div class="name">Endosteal implants</div><p class="body-copy">These are surgically implanted directly into the jawbone. Once the surrounding gum tissue has healed, a second surgery is needed to connect a post to the original implant.</p></div></div>
    <div class="type-item type-item--narrow"><svg width="10" height="10"><use href="#tooth"/></svg><div><div class="name">Subperiosteal implants</div><p class="body-copy">These consist of a metal frame that is fitted onto the jawbone just below the gum tissue. As the gums heal, the frame becomes fixed to the jawbone. Posts attached to the frame protrude through the gums.</p></div></div>
  </div>
  <div class="t promise"><b>WE BET YOU,</b>IT WON'T HURT!</div>

  <div class="t reviews">
    <div class="label"><b>WHAT</b>PEOPLE SAY</div>
    <div class="quote"><span class="quote-mark">“</span><div><p>Simply amazing and very knowledgeable. I have had my teeth cleaned in the military but she really did an amazing job.</p><cite>- Dana R, Patient</cite></div><span class="quote-mark">”</span></div>
  </div>
  <div class="t contact">
    <div class="section-title">Get in touch</div>
    <div class="lead">We'd love to hear from you</div>
    <div class="offices">
      <div class="office"><h4>Larkton, MD</h4>
        <div class="office-row"><svg width="8" height="10"><use href="#pin"/></svg><span>418 Harbor Mill Rd,<br>Larkton, MD 20700</span></div>
        <div class="office-row"><svg width="9" height="9"><use href="#phone"/></svg><span>240-555-0142<br>1-800-555-0168</span></div></div>
      <div class="office"><h4>Brookvale, MD</h4>
        <div class="office-row"><svg width="8" height="10"><use href="#pin"/></svg><span>7731 Fernway Rd,<br>Brookvale, MD 20800</span></div>
        <div class="office-row"><svg width="9" height="9"><use href="#phone"/></svg><span>301-555-0193<br>1-800-555-0177</span></div></div>
    </div>
  </div>

  <div class="t brand-name">q7r Dental</div>
  <div class="t tagline"><small>You deserve nothing less...</small><b>A Beautiful<br>Smile</b></div>
  <div class="t website">www.q7rdental.com</div>
</section>

</body>
</html>
```